1 Page Website Design For Diabetic Discount RX Card

~~I NEED A WEBSITE LANDING PAGE DESIGNED~~:

TITLE: GET UP TO 75% Off ALL YOUR DIABETIC SUPPLIES GUARANTEED
SUBITITLE: Never Pay Full Price For Your Diabetic Supplies Again!

~~FORM~~:
Choose Your Current Brand Of Diabetic Supplies That You Currently Use To See If They Are Covered Under Our Free Diabetic RX Assistance Program:

~~DROP DOWN MENU~~
Acarbose Up To 75% Off!

Verimbra Dux Up To 75% Off!

Verimbra Dux Xr Up To 54% Off!

Pelvo Up To 75% Off!

Borquell Up To 75% Off!

Tumisko Up To 75% Off!

Quisden Up To 75% Off!

Welvoke Up To 75% Off!

Zorpelline Up To 54% Off!

Zorpequin Up To 54% Off!

Zorpeta Up To 54% Off!

Calmivest Up To 75% Off!

Calmora Up To 75% Off!

Chlorpropamide Up To 75% Off!

Colesevelam Up To 75% Off!

Merrowin Up To 54% Off!

Qnrk Up To 75% Off!

Desmopressin 52% Off

Hostivel 74% Off

Pruntalex Up To 54% Off!
Sorvilk Up To 75% Off!

Delumbo Up To 75% Off!

Nuskavir Up To 75% Off!

Glimepiride 66% Off

Glipizide Up To 75% Off!

Glipizide Er Up To 75% Off!

Tremvalux Up To 75% Off!

Tremvalux Xr Up To 75% Off!

Brenzofil Up To 75% Off!

Brenzofil Xl Up To 75% Off!

Yestramor Up To 75% Off!

Kipolvan Up To 75% Off!

Glyburide Up To 75% Off!

Glyburide Micronized Up To 75% Off!
Ostrivel Up To 75% Off!

Pardow Up To 75% Off!

Vuntorek Up To 75% Off!

Restivon 50 50 Up To 75% Off!

Restivon Up To 75% Off!

Kavostra N Up To 75% Off!

Kavostra R Up To 75% Off!

Insulin Detemir Up To 75% Off!

Insulin Glulisine Up To 75% Off!

Pelsquorin Up To 75% Off!

Pelsquora Up To 75% Off!

Roblinex Up To 75% Off!

Roblinex Xr Up To 75% Off!

Roblivo Up To 75% Off!

Mespolure Up To 75% Off!

Wovrastelo Up To 75% Off!

Tilbemo Up To 75% Off!

Frastovane Xr Up To 75% Off!

Ovrink Up To 75% Off!

Sauprex Up To 75% Off!

Drunvelo Up To 54% Off!

Metformin 73% Off

Pastoquil Up To 54% Off!

Miglitol Up To 75% Off!

Ferbalick Up To 33% Off!

Nateglinide Up To 75% Off!

Ulvoria Up To 75% Off!

Zestrapol Up To 75% Off!

Zestrabin N Up To 75% Off!

Zestrabin R Up To 75% Off!

Zestrakor Up To 75% Off!

Zestraplum Up To 33% Off!

Brumvexa Up To 75% Off!

Tescavil Up To 54% Off!

Krudal Up To 75% Off!

Pioglitazone Up To 75% Off!

Pramlintide Up To 75% Off!

Wolbanix Up To 54% Off!

Wolbary Up To 75% Off!

Humbrek 20% Off

Repaglinide Up To 75% Off!

Sadvex Up To 75% Off!

Rosiglitazone Up To 75% Off!

Sitagliptin Up To 75% Off!

Plumvoy Up To 75% Off!

Garvostek Up To 75% Off!

Treskuvo Up To 75% Off!

Obrilcha Up To 75% Off!

Tolazamide Up To 75% Off!

Tolbutamide Up To 75% Off!

Vempruka Up To 54% Off!

Faskid Up To 75% Off!

Lurmobixa Up To 75% Off!

Qualmedo Up To 75% Off!

Sombrewick Up To 15% Off!

Vantoberry Up To 75% Off!

Dombrisel Up To 33% Off!

Harnupex Up To 75% Off!

Pidsarn Up To 75% Off!

Brafmel Xr Up To 75% Off!

~~~~After they choose one I want this message to pop up~~~~:

YES! ~~NAME OF DRUG~~ IS COVERED UNDER OUR FREE DIABETIC RX PROGRAM!
3 EASY WAYS TO RECEIVE YOUR FREE DIABETIC RX ASSISTANCE VOUCHER:

1. Simply Click Below To Download Your Voucher Right Now!

~~DOWNLOAD VOUCHER NOW~~
2. Enter Your Cell Phone Number And We Will Send The Voucher To You By Text Message Instantly:

3. Enter Your Email And We Will Send The Voucher To Your Email Instantly:

Target Market(s)

People with Diabetes

Number of Pages Required

1 page

Colors

Designer to choose colors to be used in the design.

Requirements
Must have
• must be professional looking and build trust and credibility
Nice to have
• Photos of diabetics...real people
Should not have
• red

```html
<!DOCTYPE html>
<html lang="en">
<head>
<meta charset="UTF-8">
<title>Diabetic RX Voucher</title>
<link rel="stylesheet" href="https://fonts.googleapis.com/css2?family=Lato:ital,wght@0,400;0,700;0,900;1,700&display=swap">
<style>
  :root {
    --page-bg: #ffffff;
    --modal-teal: #2aa6b3;
    --divider: rgba(255,255,255,0.55);
    --text-light: #ffffff;
    --button-blue: #1f87c9;
    --field-bg: #f7f7f7;
    --chevron-blue: #1f87c9;
  }
  * { box-sizing: border-box; margin: 0; padding: 0; }
  html, body {
    width: 1200px; height: 970px; overflow: hidden;
    background: var(--page-bg);
    font-family: "Lato", Arial, sans-serif;
  }
  .canvas { position: relative; width: 1200px; height: 970px; }
  .voucher-modal {
    position: absolute; left: 88px; top: 75px;
    width: 1030px; height: 825px;
    background: var(--modal-teal);
    border-radius: 24px;
    color: var(--text-light);
    text-align: center;
  }
  .close-button {
    position: absolute; right: 28px; top: -16px;
    width: 54px; height: 54px; border-radius: 50%;
    background: var(--text-light);
    display: flex; align-items: center; justify-content: center;
  }
  .headline {
    position: absolute; left: 0; right: 0; top: 122px;
    font-style: italic; font-weight: 700;
    font-size: 24px; line-height: 30px; letter-spacing: 0.3px;
    text-transform: uppercase;
  }
  .step-text {
    position: absolute; left: 0; right: 0;
    font-size: 21px; line-height: 32px; font-weight: 400;
  }
  .step-one { top: 238px; }
  .step-two { top: 412px; }
  .step-three { top: 611px; }
  .download-button {
    position: absolute; left: 400px; top: 297px;
    width: 226px; height: 54px;
    background: var(--button-blue); border-radius: 4px;
    display: flex; align-items: center; justify-content: center; gap: 14px;
    font-weight: 900; font-size: 21px; letter-spacing: 0.5px;
  }
  .download-icon {
    width: 30px; height: 30px; border-radius: 50%;
    background: var(--text-light);
    display: flex; align-items: center; justify-content: center;
  }
  .section-divider {
    position: absolute; left: 0; right: 0; height: 2px;
    background: var(--divider);
  }
  .divider-one { top: 375px; }
  .divider-two { top: 575px; }
  .send-field {
    position: absolute; left: 327px;
    width: 358px; height: 58px;
    background: var(--field-bg);
    display: flex; align-items: center; justify-content: flex-end;
    padding-right: 14px;
  }
  .phone-field { top: 485px; }
  .email-field { top: 685px; }
</style>
</head>
<body>
<div class="canvas">
  <section class="voucher-modal">
    <div class="close-button" aria-label="Close">
      <svg width="26" height="26" viewBox="0 0 26 26"><path d="M6 6 L20 20 M20 6 L6 20" stroke="var(--modal-teal)" stroke-width="5" stroke-linecap="round"/></svg>
    </div>

    <h1 class="headline">Yes! Acarbose is covered under our free diabetic RX program!<br>3 easy ways to receive your free<br>diabetic RX assistance voucher :</h1>

    <p class="step-text step-one">1. Simply click below to download your voucher right now !</p>
    <div class="download-button">DOWNLOAD
      <span class="download-icon"><svg width="16" height="12" viewBox="0 0 16 12"><path d="M3 3 L8 8 L13 3" fill="none" stroke="var(--button-blue)" stroke-width="3.5" stroke-linecap="round" stroke-linejoin="round"/></svg></span>
    </div>

    <div class="section-divider divider-one"></div>

    <p class="step-text step-two">2. Enter your Phone Number and we will send The Voucher to you<br>by text message instantly</p>
    <div class="send-field phone-field">
      <svg width="16" height="24" viewBox="0 0 16 24"><path d="M4 3 L12 12 L4 21" fill="none" stroke="var(--chevron-blue)" stroke-width="4" stroke-linecap="round" stroke-linejoin="round"/></svg>
    </div>

    <div class="section-divider divider-two"></div>

    <p class="step-text step-three">2. Enter your E-mail and we will send The Voucher to your E-mail instantly</p>
    <div class="send-field email-field">
      <svg width="16" height="24" viewBox="0 0 16 24"><path d="M4 3 L12 12 L4 21" fill="none" stroke="var(--chevron-blue)" stroke-width="4" stroke-linecap="round" stroke-linejoin="round"/></svg>
    </div>
  </section>
</div>
</body>
</html>
```